Grins Circle Brochure highlighting office, club membership, dentist to attract new members

This brochure is for prospective patients who are interested in joining our Exclusive Member Only program. The brochure should explain the exclusivity of the club, club fees, membership benefits, office hightlights, friendly staff, experienced Dentist, Also can refer to our website www.dentistkavra.example for more information to go into brochure.

Our mission is to provide a quality care your smile needs, comfort & luxury you deserve.

Staff - Our dedicated, friendly & experience staff are well equipped to answer all your questions and make every visit as memorable as the previous the one. We believe Care for your comfort is as important as Care your Smile needs. We strive to make every aspect of your visit as smooth and effortless as possible.

Dentist - Dr. Kavra, I have extensive experience in general, cosmetic & orthodontic treatments. I continue to attend continued education more than required by the dental association. My only motivation is to bring the best of the procedures and technology available in the market today for my patients. I am also a member of many professional organizations in DC metro area which helps share and promote best practices in the industry. Outside of Dentistry I love to spend time with my 6 and 2 yr olds as a nature lover I get to hike regularly, as weather gets cold, I love to hit the thread mil with my fav music. Yoga stretches are part of my in between procedures.

Office - Our office has been in the current location for over 30 years. Our office has been updated continuously, however we continue to keep the warm and relaxing ambience. The reception area is the hallmark of our core principle. The coffee station with the traditional seating helps us set the warm and cozy tone for the rest of the office. The water fountain adds the relaxing experience. Though many patients have noted they don’t get to enjoy the reception area as they don’t usually get to wait. We take that as a compliment.

Operatory
We have three operatories Meadow, Lanternwood & Bluebrook each named to reflect the essence we strive for in all aspect of our practice. Each operatory is equipped with varied softrelmic firmness for your comfort. All the operatories are kept clean and well organized for visual and functional smoothness. The technologies are kept upto date to ensure our services are unparalleled. We offer warm cotton towels during long procedures to ensure comfortness. We make individual eye shades to protect the eyes.

Restroom
Last but not the least we are proud of our restroom, we ensure our standards and attention to the details are carried through and through. Cotton towels are available to help freshen up after a long procedure.

The Club
I know you have been waiting to know about the club. I saved the best to the last. Grins Circle is the crown jewel of our practice. As part of my quest to continue to improve our services, after a considerable thought and iterations we conceived this program. The core objective is to bring another level of comfort to our patients. The program brings all the aspects of our being together in a simple package. Instead of breaking the essentials like cleaning, Xrays, Fluoride, whitening, diagnosis, consultation,emergency visits,, we simplified everything into one simple club membership. As a member of Grins Circle you will get all of the basic essentials included in your program. Also you will receive membership discounts from 15% to 25% in all the procedures. The best part of the program is all your procedures cost can be financed at 0% interest. As always our staff stay on top of your essential treatments, reaching out to you by your preferred mode of contact and ensure you get your essentials done at your convenience.

Pricing

The Grins Circle program is a subscription program. Patients pay monthly subscription. This simple monthly subscription covers all the essential routine dental care including Cleaning, XRays, Fluoride treatment, Whitening, Diagnosis, Consultation, Emergency visits.

Single membership is $59 a month
Family of Two membership is $49 per person per month
Family of Three and more is $39 per person per month

Members receive 15% to 25% discounts on all of the below procedures

Orthodontic - Clearvane, Braces
Implants
Bridges
Crowns
Tooth Extractions
Rylaxo treatments
Laser Gum Treatments
Veneers, Bonding
Fillings
Dentures

Target Market(s)

high income group, family, professionals, teens

Industry/Entity Type

Club

Font styles to use
Script

Colors
3176b5

Requirements
Must have
• Logo, pic of Dentist, office pics

```html
<!DOCTYPE html>
<html lang="en">
<head>
<meta charset="utf-8">
<title>Grins Circle Brochure – Outside Spread</title>
<link rel="stylesheet" href="https://fonts.googleapis.com/css2?family=Open+Sans:wght@400;600;700&family=Roboto:wght@400;500;700;900&family=Roboto+Condensed:wght@700&display=swap">
<style>
  :root{
    --blue-deep:#1f2f9e;
    --blue-main:#2f4fd0;
    --blue-bright:#3b62e0;
    --blue-light:#6f8ff0;
    --blue-link:#5b7ef2;
    --black:#151618;
    --charcoal:#2b2c2f;
    --silver-1:#f2f3f4;
    --silver-2:#c9cbcd;
    --green:#2c7a35;
    --white:#ffffff;
    --ink:#222;
  }
  *{margin:0;padding:0;box-sizing:border-box}
  html,body{width:1200px;height:1003px;overflow:hidden;background:#d3d5d6}
  .spread{position:relative;width:1200px;height:1003px;display:flex}
  .panel{position:relative;width:600px;height:1003px;overflow:hidden}
  .panel-bg{position:absolute;inset:0}

  /* back cover */
  .contact{position:absolute;left:0;width:576px;top:282px;text-align:center;color:var(--white);font-family:"Open Sans",sans-serif}
  .contact-title{font-family:"Open Sans",sans-serif;font-weight:700;font-size:37px;letter-spacing:.5px;color:#f0f0f0;text-shadow:0 2px 3px rgba(0,0,0,.6);margin-bottom:14px}
  .icon{display:block;margin:0 auto;width:26px;height:26px}
  .office-name{font-family:"Roboto",sans-serif;font-weight:500;font-size:21px;color:var(--blue-link);margin-top:6px;line-height:1.1}
  .office-address{font-size:14px;margin-top:3px;margin-bottom:12px}
  .phone-line{font-size:19px;line-height:1.75}
  .phone-line strong{font-weight:600}

  .brand{display:flex;align-items:center;gap:8px;justify-content:center;color:var(--white);font-family:"Roboto",sans-serif;font-weight:700}
  .brand-dot{border-radius:50%;background:var(--white)}
  .brand-back{position:absolute;left:0;width:576px;top:840px;font-size:30px}
  .brand-back .brand-dot{width:20px;height:20px}
  .tagline{font-family:"Roboto Condensed",sans-serif;font-weight:700;color:var(--white);text-transform:uppercase;text-align:center;line-height:1.25}
  .tagline-back{position:absolute;left:0;width:576px;top:927px;font-size:19px}
  .rule{position:absolute;top:961px;height:1px;background:rgba(255,255,255,.7)}

  /* front cover */
  .photo{position:absolute;border-radius:50%}
  .photo-patient{left:622px;top:62px;width:450px;height:450px}
  .photo-dentist{left:943px;top:371px;width:226px;height:226px}
  .brand-front{position:absolute;right:18px;top:70px;font-size:22px;justify-content:flex-end}
  .brand-front .brand-dot{width:16px;height:16px}
  .tagline-front{position:absolute;right:14px;top:130px;width:150px;font-size:14px}
  .headline{position:absolute;left:600px;width:600px;text-align:center;font-family:"Roboto",sans-serif}
  .headline-kicker{top:646px;font-size:24px;color:var(--ink);left:616px}
  .headline-comfort{top:684px;font-size:54px;font-weight:700;color:var(--blue-bright);left:616px;letter-spacing:-.5px}
  .headline-deserve{top:740px;font-size:76px;font-weight:900;color:var(--green);left:616px;letter-spacing:-.5px}
  .web{top:833px;font-size:20px;font-weight:700;color:var(--blue-main);letter-spacing:2.5px;left:616px}
</style>
</head>
<body>
<main class="spread">

  <!-- Back cover -->
  <section class="panel panel-back">
    <svg class="panel-bg" width="600" height="1003" viewBox="0 0 600 1003">
      <defs>
        <linearGradient id="backBlue" x1="0" y1="0" x2="1" y2="1">
          <stop offset="0" stop-color="#3a5de0"/>
          <stop offset="1" stop-color="#2342c2"/>
        </linearGradient>
        <radialGradient id="backBlack" cx=".55" cy=".5" r=".7">
          <stop offset="0" stop-color="#34353a"/>
          <stop offset="1" stop-color="#121315"/>
        </radialGradient>
      </defs>
      <rect width="600" height="1003" fill="url(#backBlue)"/>
      <path d="M0,195 C150,110 420,120 600,215 V840 H0Z" fill="var(--blue-light)"/>
      <path d="M0,215 C150,135 420,140 600,235 V840 H0Z" fill="var(--blue-main)"/>
      <path d="M0,240 C150,160 420,165 600,255 V840 C430,760 260,720 140,728 C80,732 30,742 0,754Z" fill="url(#backBlack)"/>
      <path d="M0,754 C30,742 80,732 140,728 C260,720 430,760 600,840 V872 C430,792 260,752 140,760 C80,764 30,774 0,786Z" fill="var(--white)"/>
      <path d="M0,786 C30,774 80,764 140,760 C260,752 430,792 600,872 V1003 H0Z" fill="url(#backBlue)"/>
    </svg>

    <div class="contact">
      <h2 class="contact-title">CONTACT US</h2>
      <svg class="icon" viewBox="0 0 26 26"><circle cx="13" cy="13" r="13" fill="#fff"/><path d="M13 6a5 5 0 0 0-5 5c0 4 5 9 5 9s5-5 5-9a5 5 0 0 0-5-5zm0 7a2 2 0 1 1 0-4 2 2 0 0 1 0 4z" fill="#151618"/></svg>
      <p class="office-name">GRINS OF NORTHVALE</p>
      <p class="office-address">210 Linden Crest Rd, Suite 114 Northvale, MD, United States 20000</p>
      <svg class="icon" viewBox="0 0 26 26"><circle cx="13" cy="13" r="13" fill="#fff"/><path d="M13 6a5 5 0 0 0-5 5c0 4 5 9 5 9s5-5 5-9a5 5 0 0 0-5-5zm0 7a2 2 0 1 1 0-4 2 2 0 0 1 0 4z" fill="#151618"/></svg>
      <p class="office-name">GRINS OF HARTSFIELD</p>
      <p class="office-address">88 Orchard Lane, Suite 212 Hartsfield, MD, United States 20001</p>
      <svg class="icon" viewBox="0 0 26 26" style="margin-top:10px"><circle cx="13" cy="13" r="13" fill="#fff"/><path d="M9 7c1-.6 1.8-.2 2.3.8l.8 1.6c.3.7.1 1.3-.5 1.8l-.6.5c.6 1.5 1.8 2.8 3.3 3.5l.5-.6c.5-.6 1.2-.8 1.9-.4l1.6.8c1 .5 1.3 1.4.7 2.3-.8 1.3-2.2 1.8-3.6 1.3C11.7 18.2 8.4 15 7.2 11.3 6.8 9.5 7.6 7.9 9 7z" fill="#151618"/></svg>
      <p class="phone-line" style="margin-top:6px">555-010-4821 - <strong>Northvale</strong></p>
      <p class="phone-line">555-010-7736 - <strong>Hartsfield</strong></p>
    </div>

    <div class="brand brand-back"><span class="brand-dot"></span>Grins Circle</div>
    <p class="tagline tagline-back">Excellence in care,<br>skill and judgement</p>
    <span class="rule" style="left:25px;width:180px"></span>
    <span class="rule" style="left:372px;width:228px"></span>
  </section>

  <!-- Front cover -->
  <section class="panel panel-front" style="position:absolute;left:600px;top:0">
    <svg class="panel-bg" width="600" height="1003" viewBox="0 0 600 1003">
      <defs>
        <linearGradient id="silver" x1="0" y1="0" x2="1" y2="1">
          <stop offset="0" stop-color="var(--silver-2)"/>
          <stop offset=".45" stop-color="var(--silver-1)"/>
          <stop offset="1" stop-color="#b9bcbf"/>
        </linearGradient>
        <linearGradient id="frontBlue" x1="0" y1="0" x2="1" y2="1">
          <stop offset="0" stop-color="#26389f"/>
          <stop offset="1" stop-color="#2c44b8"/>
        </linearGradient>
        <radialGradient id="badge" cx=".4" cy=".35" r=".7">
          <stop offset="0" stop-color="#ffffff"/>
          <stop offset=".7" stop-color="#d6d8da"/>
          <stop offset="1" stop-color="#9a9da1"/>
        </radialGradient>
      </defs>
      <rect width="600" height="1003" fill="url(#silver)"/>
      <path d="M0,0 H600 V290 C540,310 480,340 430,380 C330,470 200,600 0,640Z" fill="var(--blue-light)"/>
      <path d="M0,0 H600 V270 C530,295 470,330 420,370 C320,455 190,580 0,620Z" fill="url(#frontBlue)"/>
      <path d="M0,830 C150,880 300,935 440,932 C520,930 565,880 600,812 V1003 H0Z" fill="var(--black)"/>
      <path d="M0,860 C150,905 300,958 440,958 C520,956 570,912 600,850 V1003 H0Z" fill="var(--white)"/>
      <path d="M0,872 C150,918 300,970 440,972 C520,970 572,930 600,868 V1003 H0Z" fill="var(--blue-main)"/>
      <circle cx="247" cy="287" r="236" fill="var(--blue-bright)"/>
      <circle cx="456" cy="484" r="130" fill="var(--blue-main)"/>
      <circle cx="456" cy="484" r="120" fill="var(--white)"/>
      <g role="img" aria-label="Dental care icon badge">
        <circle cx="302" cy="556" r="60" fill="#b8bbbe"/>
        <circle cx="302" cy="556" r="52" fill="url(#badge)"/>
      </g>
      <g role="img" aria-label="Dental implant icon badge">
        <circle cx="302" cy="928" r="56" fill="#b8bbbe"/>
        <circle cx="302" cy="928" r="48" fill="url(#badge)"/>
      </g>
    </svg>

    <div class="photo photo-patient" role="img" aria-label="Photo of a smiling patient in the dental chair during a check-up"
         style="left:22px;top:62px;background:radial-gradient(circle at 55% 40%,#e9c3b0 0%,#b99585 35%,#8fb3d0 70%,#6d9bc7 100%)"></div>
    <div class="photo photo-dentist" role="img" aria-label="Portrait photo of Dr. Kavra in blue scrubs"
         style="left:343px;top:371px;background:radial-gradient(circle at 50% 35%,#d0a58c 0%,#b48a74 25%,#8fc4de 55%,#eef2f4 80%)"></div>

    <div class="brand brand-front"><span class="brand-dot"></span>Grins Circle</div>
    <p class="tagline tagline-front">Excellence in care,<br>skill and judgement</p>

    <p class="headline headline-kicker" style="left:16px">Care Your Smile Needs</p>
    <h1 class="headline headline-comfort" style="left:16px">COMFORT &amp; LUXURY</h1>
    <p class="headline headline-deserve" style="left:16px">YOU DESERVE</p>
    <p class="headline web" style="left:16px">www.dentistkavra.example</p>
  </section>

</main>
</body>
</html>
```